Design of a Web Development Agency

We're a web development agency (we do not offer design services). We'd like to get a new website up and running. We do custom web application development - large scale applications in the financial, healthcare, automotive, and other industries.

We need the following types of pages designed:
1) Homepage
2) Blog
3) Services page
4) Packages page
4) Generic content
5) Contact Us form.

The design should be consistent with our current icon. We're looking for a clean, corporate, brand. We'd like the design to expand on the concepts in the logo - the use of the electrical wiring motif / the colors / etc.

We offer the following services: 1) Cobalto web hosting consulting, 2) custom application development, 3) Qel development, 4) Veltrix development.

We offer packages in numbers of hours. We have about 3-4 tiers of services - the number of hours versus the monthly invoice total. For example, 5 hours per month of $500.00, for example.

Target Market(s)

Corporate clients

Industry/Entity Type

Electrical

Colors
acd036
33b7a4
33a6d7
3176b5
876aae
b768aa
fbee3e

Requirements
Must have
• Responsive / mobile friendly design.
• An email submitting form on the contact us page
Nice to have
• We'd like a bit of San Francisco to come through (where we're located)
• A plorvo map of our address on the contact us page
Should not have
• Excessive imagery. We don't have a lot of imagery, so we'd basically have to go out and find stock photography to put in it's place, which we just don't really want to do. All imagery should be supplied by the designer (we'll pay any copyright fees, if applicable, you just have to send us a list of the links to the imagery. Max budget would be $100-$200 on imagery, but preferably as little as possible).

```html
<!DOCTYPE html>
<html lang="en">
<head>
<meta charset="utf-8">
<title>Harlow Web Works</title>
<link rel="stylesheet" href="https://fonts.googleapis.com/css2?family=Ubuntu:ital,wght@0,300;0,400;0,500;0,700;1,400;1,700&display=swap">
<style>
:root{
  --green:#acd036;--teal:#33b7a4;--sky:#33a6d7;--blue:#3176b5;--purple:#876aae;--pink:#b768aa;--yellow:#fbee3e;
  --ink:#2b2b2b;--muted:#666;--light:#efefef;--dark:#2d2d2d;--footer:#1f1f1f;
}
*{box-sizing:border-box;margin:0;padding:0}
html,body{width:1200px;height:3731px;overflow:hidden}
body{font-family:'Ubuntu',sans-serif;color:var(--ink);background:#fff;position:relative}
section,header,footer{position:absolute;left:0;width:1200px}
.abs{position:absolute}
.center{text-align:center;left:0;width:1200px}

/* header */
.site-header{top:0;height:118px;background:#fff}
.brand{left:160px;top:22px;display:flex;align-items:center;gap:16px}
.brand-mark{width:74px;height:74px;border-radius:50%;background:var(--blue)}
.brand-name{font-size:17px;font-weight:500;color:var(--ink);letter-spacing:.3px;white-space:nowrap}
.main-nav{left:540px;top:50px;display:flex;gap:24px;font-size:15px;text-transform:uppercase;white-space:nowrap}
.main-nav a{text-decoration:none}
.nav-home{color:var(--purple);border-bottom:2px solid var(--purple);padding-bottom:6px}

/* hero */
.hero{top:118px;height:488px;background:linear-gradient(120deg,#111 0%,#4a4a4a 35%,#2a2a2a 60%,#777 85%,#3a3a3a 100%)}
.hero h1{top:168px;font-size:66px;font-weight:500;color:#fff;line-height:74px}

/* section titles */
.sec-title{font-size:58px;font-weight:400;letter-spacing:1px;line-height:66px}
.sec-sub{font-size:17px;color:var(--muted);line-height:22px}

/* services */
.services{top:606px;height:737px;background:var(--light)}
.services .sec-title{top:30px}
.services .sec-sub{top:98px}
.service-node{position:absolute;width:300px;text-align:center;transform:translateX(-50%)}
.service-node span{display:block;font-size:13px;margin-bottom:12px}
.dot{margin:0 auto;width:108px;height:108px;border-radius:50%;border:4px solid #fff;box-shadow:0 3px 8px rgba(0,0,0,.2);display:flex;align-items:center;justify-content:center}
.hub{position:absolute;left:404px;top:308px;width:392px;height:392px;border-radius:50%;background:var(--blue);border:6px solid #fff;box-shadow:0 4px 14px rgba(0,0,0,.2);color:#fff;text-align:center;overflow:hidden}
.hub-mark{margin:42px auto 0;width:124px;height:124px;border-radius:50%;background:rgba(255,255,255,.15)}
.hub p{font-size:13px;font-style:italic;line-height:18px;padding:20px 62px 0}

/* work */
.work{top:1343px;height:725px;background:#fff}
.work .sec-title{top:68px}
.work .sec-sub{top:136px}
.showcase{left:250px;top:210px;width:700px;height:440px;border-radius:8px;background:linear-gradient(135deg,#f3f3f3,#d9d9d9 50%,#e9c3dd)}
.arrow{font-size:34px;color:#bbb;top:384px}
.slider-dots{top:695px;display:flex;justify-content:center;gap:8px}
.slider-dots i{width:9px;height:9px;border-radius:50%;background:#ccc}
.slider-dots i:first-child{background:#888}

/* clients */
.clients{top:2068px;height:161px;background:var(--pink)}
.client-strip{left:155px;top:40px;width:890px;height:87px;background:#fff;display:flex;align-items:center;justify-content:space-around;padding:0 50px}
.client-strip span{font-size:26px;font-weight:700;color:#333}
.strip-arrow{top:66px;width:28px;height:34px;background:var(--blue);color:#fff;font-size:20px;display:flex;align-items:center;justify-content:center}

/* blog */
.blog{top:2229px;height:532px;background:var(--dark);color:#fff}
.blog .sec-title{top:54px;color:#fff}
.blog .sec-sub{top:126px;color:#777}
.avatar{position:absolute;top:218px;width:110px;height:110px;border-radius:50%;background:#555;border:5px solid #444}
.avatar.active{border-color:var(--yellow)}
.post-date{top:356px;font-size:20px;font-weight:700;font-style:italic}
.post-text{left:170px;width:860px;top:404px;font-size:13px;font-style:italic;line-height:20px;text-align:center;color:#ddd}

/* contact */
.contact{top:2761px;height:886px;background:var(--teal);color:#fff}
.contact .sec-title{top:54px;color:#fff}
.contact-lead{top:130px;font-size:17px;font-weight:700}
.map{left:161px;top:214px;width:268px;height:268px;border-radius:50%;background:linear-gradient(135deg,#e6e9e2,#c9d3c8);border:5px solid #fff}
.info{left:211px;font-size:13px;display:flex;gap:14px;align-items:flex-start}
.info svg{flex:none}
.contact-form{left:522px;top:220px;width:516px}
.row{display:flex;gap:28px;margin-bottom:18px}
.field{flex:1}
.field label{display:block;font-size:13px;margin-bottom:6px}
.field .box{height:26px;background:#fff}
.select{color:#555;font-size:12px;padding:5px 8px;display:flex;justify-content:space-between}
.message .box{height:188px}
.submit{margin-top:14px;width:187px;height:38px;background:var(--yellow);color:#333;font-weight:700;font-size:18px;letter-spacing:2px;display:flex;align-items:center;justify-content:center}

/* footer */
.site-footer{top:3647px;height:84px;background:var(--footer);color:#999}
.copyright{top:20px;font-size:12px}
.social{top:46px;display:flex;gap:8px;justify-content:center}
.social i{width:20px;height:20px;background:#fff}
.to-top{right:14px;top:20px;width:30px;height:30px;border:2px solid #777;border-radius:50%;color:#999;font-size:14px;display:flex;align-items:center;justify-content:center}
</style>
</head>
<body>

<header class="site-header">
  <div class="brand abs"><div class="brand-mark"></div><span class="brand-name">HARLOW WEB WORKS</span></div>
  <nav class="main-nav abs">
    <a class="nav-home">Home</a>
    <a style="color:var(--green)">Services</a>
    <a style="color:var(--teal)">Packages</a>
    <a style="color:var(--sky)">About Us</a>
    <a style="color:var(--purple)">Blog</a>
    <a style="color:var(--pink)">Contact Us</a>
  </nav>
</header>

<section class="hero" role="img" aria-label="Dark photograph of a desk with a laptop and coffee cup">
  <h1 class="abs center">Qel &amp; Veltrix<br>Lorem Ipsum Sit Dolor Almet</h1>
</section>

<section class="services">
  <h2 class="sec-title abs center">SERVICES</h2>
  <p class="sec-sub abs center">Lorem ipsum dolor sit amet consectetuer adipiscing elit sed diam nonummy nibh</p>
  <svg class="abs" style="left:0;top:0" width="1200" height="737" aria-hidden="true">
    <g stroke="#cfcfcf" stroke-width="2" fill="none">
      <line x1="600" y1="240" x2="600" y2="310"/>
      <path d="M311 420 Q330 500 420 520"/>
      <path d="M886 420 Q870 500 780 520"/>
      <path d="M246 660 Q300 640 410 590"/>
      <path d="M948 660 Q900 640 790 590"/>
    </g>
  </svg>
  <div class="service-node" style="left:600px;top:154px"><span style="color:var(--blue)">HARLOW WEB WORKS</span><i class="dot" style="background:var(--blue);width:100px;height:100px"></i></div>
  <div class="service-node" style="left:311px;top:284px"><span style="color:var(--teal)">Custom Application Development</span><i class="dot" style="background:var(--teal)"><svg width="46" height="36" viewBox="0 0 46 36"><rect x="2" y="2" width="42" height="32" rx="3" fill="none" stroke="#fff" stroke-width="3"/><path d="M16 12l-6 6 6 6M30 12l6 6-6 6" stroke="#fff" stroke-width="3" fill="none"/></svg></i></div>
  <div class="service-node" style="left:886px;top:284px"><span style="color:var(--purple)">Qel Development</span><i class="dot" style="background:var(--purple)"><svg width="28" height="46" viewBox="0 0 28 46"><rect x="2" y="2" width="24" height="42" rx="4" fill="none" stroke="#fff" stroke-width="3"/><circle cx="14" cy="37" r="2.5" fill="#fff"/></svg></i></div>
  <div class="hub"><div class="hub-mark"></div><p>Lorem ipsum dolor sit amet, consectetuer adipiscing elit, sed diam nonummy nibh euismod tincidunt ut laoreet dolore magna aliquam erat volutpat. Ut wisi enim ad minim veniam, quis nostrud exerci tation ullamcorper suscipit nisl ut aliquip ex ea commodo.</p></div>
  <div class="service-node" style="left:246px;top:520px"><span style="color:var(--green)">Cobalto Web Hosting Consulting</span><i class="dot" style="background:var(--green)"><svg width="46" height="40" viewBox="0 0 46 40"><rect x="2" y="2" width="42" height="28" fill="none" stroke="#fff" stroke-width="3"/><path d="M16 38h14M23 30v8" stroke="#fff" stroke-width="3"/></svg></i></div>
  <div class="service-node" style="left:948px;top:520px"><span style="color:var(--pink)">Veltrix Development</span><i class="dot" style="background:var(--pink)"><svg width="28" height="46" viewBox="0 0 28 46"><rect x="2" y="2" width="24" height="42" rx="4" fill="none" stroke="#fff" stroke-width="3"/><circle cx="14" cy="37" r="2.5" fill="#fff"/></svg></i></div>
</section>

<section class="work">
  <h2 class="sec-title abs center">HERE IS SOME OF OUR WORK</h2>
  <p class="sec-sub abs center">Lorem ipsum dolor sit amet, consectetuer adipiscing elit, sed diam nonummy nibh euismo tincidunt ut laoreet dolore</p>
  <div class="showcase abs" role="img" aria-label="Website shown on desktop, tablet and phone screens with pink paint splash"></div>
  <span class="arrow abs" style="left:140px">&#8249;</span>
  <span class="arrow abs" style="left:1042px">&#8250;</span>
  <div class="slider-dots abs center"><i></i><i></i><i></i><i></i></div>
</section>

<section class="clients">
  <div class="strip-arrow abs" style="left:141px">&#8249;</div>
  <div class="client-strip abs"><span>Meadowline</span><span>Ledgerly</span><span>Vantora</span><span>Brickwell</span><span>Stagewise</span></div>
  <div class="strip-arrow abs" style="left:1031px">&#8250;</div>
</section>

<section class="blog">
  <h2 class="sec-title abs center">BLOG POSTS</h2>
  <p class="sec-sub abs center">Lorem ipsum dolor sit amet, consectetuer adipiscing elit, sed diam nonummy nibh euismo tincidunt</p>
  <div class="avatar" style="left:178px" role="img" aria-label="Author portrait"></div>
  <div class="avatar" style="left:365px" role="img" aria-label="Author portrait"></div>
  <div class="avatar active" style="left:545px" role="img" aria-label="Author portrait"></div>
  <div class="avatar" style="left:729px" role="img" aria-label="Author portrait"></div>
  <div class="avatar active" style="left:909px" role="img" aria-label="Author portrait"></div>
  <svg class="abs" style="left:0;top:0" width="1200" height="532" aria-hidden="true">
    <g fill="none" stroke="var(--yellow)" stroke-width="7">
      <path d="M233 207 A66 66 0 0 1 299 273"/>
      <path d="M420 207 A66 66 0 0 1 486 273"/>
      <path d="M784 207 A66 66 0 0 1 850 273"/>
    </g>
  </svg>
  <p class="post-date abs center">08/11/2014</p>
  <p class="post-text abs">Lorem ipsum dolor sit amet, consectetuer adipiscing elit, sed diam nonummy nibh euismod tincidunt ut laoreet dolore magna aliquam erat volutpat. Ut wisi enim ad minim veniam, quis nostrud exerci tation ullamcorper suscipit lobortis nisl ut aliquip ex ea commodo consequat. Duis autem vel eum iriure dolor in hendrerit in vulputate velit esse molestie consequat, vel illum dolore eu feugiat nulla facilisis at vero eros et accumsan et iusto odio dignissim qui blandit praesent luptatum zzril delenit augue duis dolore te feugait nulla facilisi.</p>
</section>

<section class="contact">
  <h2 class="sec-title abs center">CONTACTUS</h2>
  <p class="contact-lead abs center">Please take a quick moment to complete this form and a business representative will get back to you soon.</p>
  <div class="map abs" role="img" aria-label="Street map of the office location"></div>
  <div class="info abs" style="top:494px"><svg width="16" height="16" viewBox="0 0 16 16"><path d="M1 8L8 2l7 6v7H1z" fill="#333"/></svg><span>Lorem ipsum dolor sit amet,<br>adipiscing elit.</span></div>
  <div class="info abs" style="top:545px"><svg width="16" height="16" viewBox="0 0 16 16"><circle cx="8" cy="8" r="8" fill="#333"/><path d="M5 4l2 2-1 1 3 3 1-1 2 2-2 1C7 11 5 9 4 6z" fill="#fff"/></svg><span>123-456-7890</span></div>
  <div class="info abs" style="top:588px"><svg width="16" height="16" viewBox="0 0 16 16"><circle cx="8" cy="8" r="8" fill="#333"/><rect x="4" y="5" width="8" height="6" fill="#fff"/></svg><span>hello@harlowwebworks.com</span></div>
  <form class="contact-form abs">
    <div class="row"><div class="field"><label>* First Name</label><div class="box"></div></div><div class="field"><label>* Last Name</label><div class="box"></div></div></div>
    <div class="row"><div class="field"><label>* Email</label><div class="box"></div></div><div class="field"><label>* Phone</label><div class="box"></div></div></div>
    <div class="row"><div class="field"><label>Company</label><div class="box"></div></div><div class="field"><label>* State</label><div class="box select"><span>- Select State -</span><span>&#9662;</span></div></div></div>
    <div class="field message"><label>Your Message</label><div class="box"></div></div>
    <div class="submit">SUBMIT</div>
  </form>
</section>

<footer class="site-footer">
  <p class="copyright abs center">Copyright &copy; 2014 Harlow Web Works. All Rights Reserved.</p>
  <div class="social abs center"><i></i><i></i><i></i><i></i></div>
  <div class="to-top abs">&#8963;</div>
</footer>

</body>
</html>
```